HOME IMPROVEMENT Business Card

I want a very unique business card. nothing typical and boring. Im open to you ideas. Ive seen cards with gold and silver or color foil and spot UV coatings. Im looking for something that looks cool and grabs attention. I like rounded corners but am open to all suggestions. We are a home improvement company and I will have a presentation folder printed and a catalog printed also and want to keep that same theme. I love the colors in our logo but I am open at looking at a 3rd color that would work with my logo. I hope that helps.
Card should include
Address
Phone
Fax
Email
Website
Target Market(s)
Home owners, people looking to remodel their home
Industry/Entity Type
Home Improvement
Contact Information for Business Card
2873 Maple Crest Avenue Unit 410
Brookvale, Oh 60284
Phone
Direct Line
Email
Website
Font styles to use
Other font styles liked:
- IM OPEN MINDED
Requirements
Must have
- High end quality look nothing boring I like rounded corners but am open minded
Nice to have
- WOW. I want something nice and impressive.
Should not have
- ??? Not sure

```html
<!DOCTYPE html>
<html lang="en">
<head>
<meta charset="utf-8">
<title>Keystead Renovation Group – Business Card</title>
<link href="https://fonts.googleapis.com/css2?family=Open+Sans:wght@400;600;700&display=swap" rel="stylesheet">
<style>
  :root {
    --stage: #2a2a2c;
    --paper: #ffffff;
    --green: #0f9a4a;
    --navy: #23215e;
    --ink: #1c1c1c;
    --muted: #4a4a4a;
  }
  * { box-sizing: border-box; margin: 0; padding: 0; }
  html, body {
    width: 1200px; height: 1000px; overflow: hidden;
    background: var(--stage);
    font-family: "Open Sans", Arial, sans-serif;
  }
  .card {
    position: absolute;
    width: 560px; height: 320px;
    border-radius: 28px;
    overflow: hidden;
    background: var(--paper);
    box-shadow: 0 10px 30px rgba(0,0,0,.45);
  }

  /* Front */
  .card-front { left: 120px; top: 80px; }
  .brand {
    position: absolute;
    display: flex; align-items: center; gap: 12px;
    color: var(--navy);
    font-weight: 700;
    white-space: nowrap;
  }
  .card-front .brand { left: 130px; top: 92px; font-size: 34px; }
  .brand-square { width: 22px; height: 22px; background: var(--green); flex: none; }
  .brand-sub { display: block; }
  .card-front .brand-name { line-height: 1.1; }
  .front-rule-right {
    position: absolute; right: 0; top: 168px;
    width: 150px; height: 9px; background: var(--green);
  }
  .front-web {
    position: absolute; left: 250px; top: 232px;
    font-size: 14px; letter-spacing: 4px; color: var(--muted);
  }
  .front-rule-short {
    position: absolute; left: 150px; top: 262px;
    width: 180px; height: 8px; background: var(--green);
  }
  .front-rule-long {
    position: absolute; left: 0; top: 292px;
    width: 330px; height: 8px; background: var(--green);
  }

  /* Back */
  .card-back { left: 520px; top: 540px; }
  .back-panel {
    position: absolute; left: 300px; top: 0;
    width: 260px; height: 320px; background: var(--green);
  }
  .address-band {
    position: absolute; left: 268px; top: 36px;
    width: 292px; height: 58px;
    background: var(--navy);
    color: #fff;
    font-size: 14px; line-height: 1.35;
    padding: 10px 0 0 50px;
  }
  .address-band::before {
    content: ""; position: absolute; left: 0; top: 0;
    border-top: 58px solid var(--paper);
    border-right: 32px solid transparent;
  }
  .card-back .brand {
    left: 330px; top: 160px; font-size: 27px;
    flex-direction: column; align-items: flex-start; gap: 0;
  }
  .card-back .brand-sub { font-size: 27px; }
  .holder-mark {
    position: absolute; left: 0; top: 92px;
    width: 48px; height: 50px; background: var(--green);
  }
  .holder-name {
    position: absolute; left: 64px; top: 88px;
    color: var(--green); font-weight: 700; font-size: 22px;
    letter-spacing: .3px;
  }
  .holder-title {
    position: absolute; left: 64px; top: 118px;
    color: var(--ink); font-weight: 600; font-size: 15px;
  }
  .contact-list {
    position: absolute; left: 44px; top: 196px;
    list-style: none;
    font-size: 15px; color: var(--ink);
  }
  .contact-list li {
    display: flex; align-items: center; gap: 12px;
    height: 24px;
  }
  .contact-list svg { width: 14px; height: 14px; fill: var(--green); flex: none; }
  .accent { color: var(--green); }
</style>
</head>
<body>

<section class="card card-front" aria-label="Business card front">
  <div class="brand">
    <span class="brand-square"></span>
    <span class="brand-name">Keystead Renovation</span>
  </div>
  <div class="front-rule-right"></div>
  <p class="front-web">www.keystead.com</p>
  <div class="front-rule-short"></div>
  <div class="front-rule-long"></div>
</section>

<section class="card card-back" aria-label="Business card back">
  <div class="back-panel"></div>
  <div class="address-band">
    2873 Maple Crest Avenue Unit 410<br>
    Brookvale, Oh 60284
  </div>
  <div class="brand">
    <span class="brand-name">Keystead</span>
    <span class="brand-sub">Renovation</span>
  </div>

  <div class="holder-mark"></div>
  <h1 class="holder-name">DANIEL BROOKS</h1>
  <p class="holder-title">CEO/FOUNDER</p>

  <ul class="contact-list">
    <li>
      <svg viewBox="0 0 16 16" aria-hidden="true"><path d="M3.6 1.5l2.3 2.6-1.3 1.6c.9 2 2.6 3.7 4.6 4.6l1.6-1.3 2.6 2.3-1.4 2.2C7 13.2 2.8 9 1.5 3.4z"/></svg>
      <span>000 000 0000</span>
    </li>
    <li>
      <svg viewBox="0 0 16 16" aria-hidden="true"><path d="M4 1h6l2 2v3h2v8H2V6h2zm1 1v4h6V3.5L9.5 2zM4 9v1h2V9zm3 0v1h2V9zm3 0v1h2V9z"/></svg>
      <span>000 000 0000</span>
    </li>
    <li>
      <svg viewBox="0 0 16 16" aria-hidden="true"><path d="M1 3h14v10H1zm1.5 1.2L8 8.6l5.5-4.4z"/></svg>
      <span>info@keystead.com</span>
    </li>
    <li>
      <svg viewBox="0 0 16 16" aria-hidden="true"><path d="M8 1a7 7 0 1 0 0 14A7 7 0 0 0 8 1zm0 1.5c.8 0 1.7 1.6 2 4H6c.3-2.4 1.2-4 2-4zm-3.5 4H2.7a5.5 5.5 0 0 1 3-3.6c-.6 1-1 2.2-1.2 3.6zm0 3c.2 1.4.6 2.6 1.2 3.6a5.5 5.5 0 0 1-3-3.6zm1.5 0h4c-.3 2.4-1.2 4-2 4s-1.7-1.6-2-4zm5.5 0h1.8a5.5 5.5 0 0 1-3 3.6c.6-1 1-2.2 1.2-3.6zm0-3c-.2-1.4-.6-2.6-1.2-3.6a5.5 5.5 0 0 1 3 3.6z"/></svg>
      <span>www.<span class="accent">keystead</span>.com</span>
    </li>
  </ul>
</section>

</body>
</html>
```